Plumbing & Heating company

A leaflet containing -

Company name - Brackenfold Plumbing Solutions
logo
Mobile number - 07700 914226
Landline - 01632 870512
Email - Info@brackenfoldplumbing.example.co.uk
website - Brackenfold-plumbing.example.co.uk
Social media logos - pixgram, Chatterly

services we offer

- Boiler replacements (free quote)
- General plumbing & heating
- Tap replacements
- 1st & 2nd
- New builds & Extensions
- Cylinder replcemets

```html
<!DOCTYPE html>
<html lang="en">
<head>
<meta charset="utf-8">
<title>Brackenfold Plumbing Solutions – Leaflet</title>
<link href="https://fonts.googleapis.com/css2?family=Oswald:wght@700&family=Montserrat:wght@600;700;800&display=swap" rel="stylesheet">
<style>
  :root{
    --navy:#0b3868;
    --navy-deep:#0d3563;
    --navy-light:#1d4f86;
    --yellow:#ffc20e;
    --paper:#f4f4f4;
    --service-bg:#ececec;
    --ink:#173a6a;
    --white:#ffffff;
  }
  *{margin:0;padding:0;box-sizing:border-box}
  html,body{width:1196px;height:1200px;overflow:hidden;background:var(--white)}
  .leaflet{position:relative;width:1196px;height:1200px;overflow:hidden;font-family:"Montserrat",sans-serif}
  .hero{position:absolute;left:0;top:0;width:1196px;height:702px}
  .hero-shapes{position:absolute;inset:0}
  .brand{position:absolute;left:62px;top:58px;display:flex;align-items:center;gap:18px}
  .brand-dot{width:64px;height:64px;border-radius:50%;background:var(--navy)}
  .brand-name{font-family:"Montserrat",sans-serif;font-weight:800;color:var(--navy);font-size:34px;line-height:1.12;letter-spacing:1px;text-transform:uppercase}
  .headline{position:absolute;left:27px;top:296px;font-family:"Oswald",sans-serif;font-weight:700;color:var(--yellow);font-size:76px;line-height:92px;text-transform:uppercase;letter-spacing:.5px}
  .services{position:absolute;left:0;top:702px;width:1196px;height:333px;background:var(--service-bg);color:var(--ink)}
  .services-title{position:absolute;top:34px;width:100%;text-align:center;font-weight:700;font-size:29px;letter-spacing:.5px}
  .service-list{position:absolute;list-style:none;font-weight:700;font-size:29px;line-height:36px;text-transform:uppercase}
  .service-list li{white-space:nowrap}
  .col-left{left:37px;top:126px}
  .col-left li{margin-bottom:12px}
  .col-left .sub{display:block;padding-left:22px}
  .col-right{left:651px;top:126px}
  .col-right li{margin-bottom:12px}
  .contact-bar{position:absolute;left:0;top:1035px;width:1196px;height:165px;background:var(--navy-deep);display:flex;align-items:center;justify-content:space-between;padding:0 28px 0 34px;color:var(--white)}
  .contact{display:flex;align-items:center;gap:14px}
  .contact svg{flex:none}
  .phones{font-weight:600;font-size:30px;line-height:42px}
  .link-text{font-weight:600;font-size:18px}
</style>
</head>
<body>
<div class="leaflet">
  <section class="hero">
    <svg class="hero-shapes" width="1196" height="702" viewBox="0 0 1196 702">
      <defs>
        <linearGradient id="paperFade" x1="0" y1="0" x2="0" y2="1">
          <stop offset="0" stop-color="#ffffff"/>
          <stop offset="1" stop-color="#ececec"/>
        </linearGradient>
        <linearGradient id="roomTone" x1="0" y1="0" x2="1" y2="1">
          <stop offset="0" stop-color="#f2f2f0"/>
          <stop offset=".55" stop-color="#e4e3e0"/>
          <stop offset="1" stop-color="#b9a089"/>
        </linearGradient>
      </defs>
      <rect width="1196" height="702" fill="url(#paperFade)"/>
      <polygon points="0,258 600,258 500,702 0,702" fill="var(--navy)"/>
      <polygon points="600,258 660,258 470,702 430,702" fill="var(--navy-light)"/>
      <polygon points="640,0 1196,0 1196,702 436,702" fill="url(#roomTone)" role="img" aria-label="Photo of an installed wall-hung boiler and hot water cylinder with copper pipework"/>
    </svg>
    <div class="brand">
      <span class="brand-dot"></span>
      <div class="brand-name">Brackenfold<br>Plumbing Solutions</div>
    </div>
    <h1 class="headline">Ensuring<br>comfort and<br>efficiency for<br>your home</h1>
  </section>

  <section class="services">
    <h2 class="services-title">SERVICES WE OFFER</h2>
    <ul class="service-list col-left">
      <li>- Boiler replacements<span class="sub">(Free quote)</span></li>
      <li>- General plumbing &amp; heating</li>
      <li>- Tap replacements</li>
    </ul>
    <ul class="service-list col-right">
      <li>- 1st &amp; 2nd</li>
      <li>- New builds &amp; extensions</li>
      <li>- Cylinder replcemets</li>
    </ul>
  </section>

  <footer class="contact-bar">
    <div class="contact">
      <svg width="50" height="46" viewBox="0 0 50 46" aria-hidden="true">
        <path d="M4 14 C4 6 46 6 46 14 L46 19 L36 19 L35 14 L15 14 L14 19 L4 19 Z" fill="var(--yellow)"/>
        <path d="M16 18 L34 18 L44 34 L44 42 L6 42 L6 34 Z" fill="var(--yellow)"/>
        <circle cx="25" cy="31" r="6" fill="var(--navy-deep)"/>
      </svg>
      <div class="phones">07700 914226<br>01632 870512</div>
    </div>
    <div class="contact">
      <svg width="36" height="36" viewBox="0 0 36 36" aria-hidden="true">
        <circle cx="18" cy="18" r="15" fill="none" stroke="var(--yellow)" stroke-width="3"/>
        <ellipse cx="18" cy="18" rx="6.5" ry="15" fill="none" stroke="var(--yellow)" stroke-width="2.5"/>
        <line x1="3" y1="18" x2="33" y2="18" stroke="var(--yellow)" stroke-width="2.5"/>
      </svg>
      <span class="link-text">Brackenfold-plumbing.example.co.uk</span>
    </div>
    <div class="contact">
      <svg width="44" height="32" viewBox="0 0 44 32" aria-hidden="true">
        <rect x="2" y="2" width="40" height="28" rx="2" fill="none" stroke="var(--yellow)" stroke-width="3"/>
        <path d="M3 4 L22 19 L41 4" fill="none" stroke="var(--yellow)" stroke-width="3"/>
      </svg>
      <span class="link-text">Info@brackenfoldplumbing.example.co.uk</span>
    </div>
  </footer>
</div>
</body>
</html>
```